KTRWG Promotion Flyer to raise money and communicate our goals

We need a flyer that promotes our organization. We are a 501(c)3 trying to raise money for Arts, Education and Entrepreneurship in our small town.

We promote a social events that improve qualtiy of life and educate people on how to start and expand businesses. Our goal is to make downtown an active and thriving place with many things for people to do and enjoy as well as create a favorable place for business.

Target Market(s)

Wealthy donors and Organizations with cash

Industry/Entity Type

Education

Colors

Designer to choose colors to be used in the design.

Requirements
Must have
• Eye catching graphics and look very professional
• Should appeal to men and women
Nice to have
• Make use of any known psychological colors and fonts etc... that appeal to philanthropic people
Should not have
• Should not be complicated or confusing

```html
<!DOCTYPE html>
<html lang="en">
<head>
<meta charset="utf-8">
<title>KTRWG Flyer</title>
<link rel="stylesheet" href="https://fonts.googleapis.com/css2?family=Lato:wght@400;700;900&family=Cinzel:wght@400&display=swap">
<style>
  :root {
    --pink: #e0237a;
    --pink-light: #ec5b95;
    --green: #8dc63f;
    --blue: #1ba1dd;
    --white: #ffffff;
    --stage: #c7c8ca;
    --ink-blue: #1d9bd7;
    --ink-dark: #3a3a3a;
  }
  * { margin: 0; padding: 0; box-sizing: border-box; }
  html, body { width: 1200px; height: 771px; overflow: hidden; background: var(--stage); }
  body { position: relative; font-family: "Lato", sans-serif; color: var(--white); }

  .page {
    position: absolute; top: 28px; width: 556px; height: 719px; overflow: hidden;
    box-shadow: 3px 4px 6px rgba(0,0,0,0.25);
  }
  .page--front { left: 28px; background: var(--pink); }
  .page--back { left: 616px; background: var(--blue); }
  .page svg.shapes { position: absolute; inset: 0; }

  /* front */
  .brand { position: absolute; left: 101px; top: 42px; width: 200px; text-align: center; color: var(--ink-dark); }
  .brand__mark { display: flex; align-items: center; justify-content: center; gap: 6px; font-weight: 700; font-size: 18px; line-height: 22px; color: var(--blue); }
  .brand__mark .dot { width: 11px; height: 11px; background: var(--pink); }
  .brand__name { font-size: 24px; font-weight: 400; line-height: 26px; margin-top: 16px; color: var(--ink-dark); }
  .brand__sub { font-family: "Cinzel", serif; font-size: 7px; letter-spacing: 0.4px; line-height: 9px; margin-top: 2px; }

  .headline { position: absolute; right: 19px; top: 75px; text-align: right; font-size: 16.5px; line-height: 19.6px; font-weight: 400; }
  .headline .pink { color: var(--pink); }
  .headline .blue { color: var(--ink-blue); }

  .intro { position: absolute; left: 70px; width: 416px; top: 517px; text-align: center; font-size: 15.6px; line-height: 19.6px; }
  .btn { position: absolute; display: flex; align-items: center; justify-content: center; color: var(--white); border-radius: 4px; letter-spacing: 0.2px; }
  .btn--join { left: 56px; top: 668px; width: 444px; height: 32px; background: var(--green); font-size: 16.4px; }

  /* back */
  .pillar__tag { position: absolute; left: 42px; width: 90px; height: 21px; background: var(--pink); font-weight: 700; font-size: 13.5px; padding-left: 7px; line-height: 21px; }
  .pillar__text { position: absolute; left: 148px; width: 372px; font-size: 13.4px; line-height: 16.4px; }
  .appeal { position: absolute; left: 42px; width: 476px; top: 484px; font-size: 13.4px; line-height: 16.4px; }
  .btn--donate { left: 137px; top: 641px; width: 296px; height: 31px; background: var(--pink); font-size: 16.5px; }
</style>
</head>
<body>

<section class="page page--front">
  <svg class="shapes" width="556" height="719" viewBox="0 0 556 719">
    <defs>
      <linearGradient id="sky" x1="0" y1="0" x2="0" y2="1">
        <stop offset="0" stop-color="#3da4e3"/>
        <stop offset="0.35" stop-color="#a9d6f0"/>
        <stop offset="0.5" stop-color="#8ab07a"/>
        <stop offset="1" stop-color="#4f8a3a"/>
      </linearGradient>
      <linearGradient id="pinkFade" x1="0" y1="0" x2="0" y2="1">
        <stop offset="0" stop-color="#ea5b98"/>
        <stop offset="1" stop-color="#e0237a"/>
      </linearGradient>
    </defs>
    <rect class="photo" role="img" aria-label="Photo of the town event hall with a white gazebo, lawn, young trees and footpath" x="0" y="0" width="556" height="540" fill="url(#sky)"/>
    <path d="M0,0 L0,66 C50,130 140,158 215,152 C255,149 290,135 320,110 L20,0 Z" fill="var(--pink)"/>
    <path d="M215,152 C300,146 375,75 422,0 L393,0 C360,70 300,142 215,146 Z" fill="var(--green)"/>
    <path d="M20,0 C40,110 130,150 215,146 C300,142 360,70 393,0 Z" fill="var(--white)"/>
    <path d="M0,528 C150,478 380,458 556,462 L556,719 L0,719 Z" fill="var(--green)"/>
    <path d="M0,540 C150,490 380,472 556,484 L556,719 L0,719 Z" fill="url(#pinkFade)"/>
  </svg>

  <div class="brand">
    <div class="brand__mark"><span class="dot"></span>KTRWG</div>
    <div class="brand__name">Maple Crossing</div>
    <div class="brand__sub">SMALL BUSINESS ASSOCIATION</div>
  </div>

  <h1 class="headline">
    <span class="pink">ARTS, EDUCATION<br>AND</span><br>
    <span class="blue">ENTREPRENEURSHIP<br>IN MAPLE CROSSING</span>
  </h1>

  <p class="intro">The Maple Crossing Small Business Association (KTRWG) is a local leader in the areas of Arts, Education and Entrepreneurship and is working diligently to promote Maple Crossing and revitalize our downtown. When you become an KTRWG Member, you will be a part of the citywide work that the KTRWG does every day to improve the lives of citizens of Maple Crossing.</p>

  <div class="btn btn--join">JOIN US TODAY! AND BE A PART OF CAMPAIGN</div>
</section>

<section class="page page--back">
  <svg class="shapes" width="556" height="719" viewBox="0 0 556 719">
    <defs>
      <linearGradient id="forest" x1="0" y1="0" x2="1" y2="1">
        <stop offset="0" stop-color="#3f4a2a"/>
        <stop offset="0.45" stop-color="#b9b98a"/>
        <stop offset="0.7" stop-color="#6f8a34"/>
        <stop offset="1" stop-color="#4d6b22"/>
      </linearGradient>
    </defs>
    <rect class="photo" role="img" aria-label="Photo of a sunlit pine forest with mossy ground" x="0" y="0" width="556" height="340" fill="url(#forest)"/>
    <path d="M0,325 C150,270 380,250 556,262 L556,719 L0,719 Z" fill="var(--green)"/>
    <path d="M0,336 C150,283 380,268 556,303 L556,719 L0,719 Z" fill="var(--blue)"/>
  </svg>

  <span class="pillar__tag" style="top:338px">We promote</span>
  <p class="pillar__text" style="top:335px">Maple Crossing Hotels, Shopping and Events that make Maple Crossing a pleasant, exciting and prosperous place to live.</p>
  <span class="pillar__tag" style="top:368px">We provide</span>
  <p class="pillar__text" style="top:368px">Training and resources to anyone interested Arts, Education and Entrepreneurship.</p>
  <span class="pillar__tag" style="top:403px">We help</span>
  <p class="pillar__text" style="top:401px">Entrepreneur's start and grow their businesses in a tax efficient and appropriate way.</p>
  <span class="pillar__tag" style="top:434px">We work</span>
  <p class="pillar__text" style="top:434px">With all levels of local government to promote our community and create a fertile environment for growth.</p>

  <p class="appeal">Every day, we look for ways to help our local businesses grow and expand, but we need you by our side. As an KTRWG Member, you can help provide training, education and support, and you can give our many businesses a chance to grow and our citizens the opportunity to experience big town amenities and events in a small town. Members' regular monthly gifts provide a consistent, reliable income stream that allows us to spend less time fundraising—and more time helping our businesses and community. Becoming an KTRWG Member is an easy, efficient and tax-deductible way to make a difference for our community all year long.</p>

  <div class="btn btn--donate">PLEASE DONATE TODAY.</div>
</section>

</body>
</html>
```